Overhead Menu Design for a Matcha Business

Hello, we are a Matcha startup and we need a designer to design an overhead menu for the next farmers market. Each menu item is to stand alone, similar to a square poster for each item (refer to rough sketches for visual explanation). Requirements:- Title of each item should be large enough to be read from a distance.- Leave a space on the bottom of each square poster so we can hand write the prices- Drawings should be simple/minimalistic (refer to inspirations)Total menu items: 6Matcha Latte - Iced (Flavors include Original, and Coconut)Matcha Latte - HotMatcha Shot - Iced (Flavors include Original, Peach, Green Apple, and Passion Fruit)Matcha Shot - HotMatcha Ice CreamMatcha BrownieWe look forward to working with you!

Target Market(s)

Customers at an outdoor market

Colors
acd036
cadf82
9bcb3b

Requirements
Must have
• Minimal + Modern + Simple

```html
<!DOCTYPE html>
<html lang="en">
<head>
<meta charset="UTF-8">
<title>Matcha Overhead Menu</title>
<link rel="stylesheet" href="https://fonts.googleapis.com/css2?family=Fira+Sans+Extra+Condensed:wght@600;700&display=swap">
<style>
  :root {
    --matcha: #acd036;
    --matcha-soft: #cadf82;
    --matcha-deep: #9bcb3b;
    --card: #ffffff;
    --backdrop: #e6e6e6;
    --icon-fill: #e3efbe;
  }
  * { margin: 0; padding: 0; box-sizing: border-box; }
  html, body { width: 1200px; height: 1000px; overflow: hidden; }
  body {
    background: var(--backdrop);
    font-family: "Fira Sans Extra Condensed", "Arial Narrow", sans-serif;
    position: relative;
  }
  .menu-card {
    position: absolute;
    width: 272px;
    height: 272px;
    background: var(--card);
    box-shadow: 0 2px 6px rgba(0,0,0,0.18);
  }
  .menu-card__frame {
    position: absolute;
    inset: 8px;
    border: 2px solid var(--matcha-soft);
    border-radius: 10px;
  }
  .menu-card__title {
    position: absolute;
    top: 14px;
    left: 0; right: 0;
    text-align: center;
    color: var(--matcha);
    font-weight: 700;
    font-size: 27px;
    line-height: 26px;
    letter-spacing: 0.5px;
  }
  .menu-card__variant {
    display: block;
    font-size: 21px;
    line-height: 22px;
    letter-spacing: 2.5px;
  }
  .menu-card__icon {
    position: absolute;
    left: 96px;
    width: 80px;
    height: 90px;
    background: var(--icon-fill);
    border-radius: 8px;
  }
  .menu-card__icon--with-variant { top: 84px; }
  .menu-card__icon--solo { top: 70px; height: 110px; left: 96px; }
  .menu-card__flavors {
    position: absolute;
    top: 180px;
    left: 0; right: 0;
    text-align: center;
    color: var(--matcha);
    font-weight: 700;
    font-size: 13px;
    line-height: 14px;
    letter-spacing: 1.2px;
  }
  .menu-card__flavors-label { display: block; letter-spacing: 2px; }
  .menu-card__flavors--compact { font-size: 12px; letter-spacing: 0.6px; }
  .menu-card__price {
    position: absolute;
    left: 20px; right: 20px;
    top: 220px;
    height: 36px;
    border: 2.5px solid var(--matcha-deep);
    border-radius: 8px;
  }
  .col-left { left: 297px; }
  .col-right { left: 629px; }
  .row-1 { top: 57px; }
  .row-2 { top: 360px; }
  .row-3 { top: 668px; }
</style>
</head>
<body>
  <section class="menu-card col-left row-1">
    <div class="menu-card__frame"></div>
    <h2 class="menu-card__title">MATCHA LATTE<span class="menu-card__variant">ICED</span></h2>
    <div class="menu-card__icon menu-card__icon--with-variant" role="img" aria-label="Iced drink glass with straw icon"></div>
    <p class="menu-card__flavors"><span class="menu-card__flavors-label">FLAVORS:</span>•Original &nbsp;•Coconut</p>
    <div class="menu-card__price"></div>
  </section>

  <section class="menu-card col-right row-1">
    <div class="menu-card__frame"></div>
    <h2 class="menu-card__title">MATCHA SHOT<span class="menu-card__variant">ICED</span></h2>
    <div class="menu-card__icon menu-card__icon--with-variant" role="img" aria-label="Iced drink glass with straw icon"></div>
    <p class="menu-card__flavors menu-card__flavors--compact" style="top:174px"><span class="menu-card__flavors-label">FLAVORS:</span>•Original •Peach<br>•Green Apple •Passion Fruit</p>
    <div class="menu-card__price"></div>
  </section>

  <section class="menu-card col-left row-2">
    <div class="menu-card__frame"></div>
    <h2 class="menu-card__title">MATCHA LATTE<span class="menu-card__variant">HOT</span></h2>
    <div class="menu-card__icon menu-card__icon--with-variant" role="img" aria-label="Steaming hot cup icon" style="width:110px;left:81px"></div>
    <p class="menu-card__flavors"><span class="menu-card__flavors-label">FLAVORS:</span>•Original &nbsp;•Coconut</p>
    <div class="menu-card__price"></div>
  </section>

  <section class="menu-card col-right row-2">
    <div class="menu-card__frame"></div>
    <h2 class="menu-card__title" style="top:28px">MATCH ICE CREAM</h2>
    <div class="menu-card__icon menu-card__icon--solo" role="img" aria-label="Ice cream cone icon" style="width:60px;left:106px"></div>
    <div class="menu-card__price"></div>
  </section>

  <section class="menu-card col-left row-3">
    <div class="menu-card__frame"></div>
    <h2 class="menu-card__title">MATCHA SHOT<span class="menu-card__variant">HOT</span></h2>
    <div class="menu-card__icon menu-card__icon--with-variant" role="img" aria-label="Small steaming hot cup icon" style="width:70px;left:101px"></div>
    <p class="menu-card__flavors"><span class="menu-card__flavors-label">FLAVORS:</span>•Original &nbsp;•Coconut</p>
    <div class="menu-card__price"></div>
  </section>

  <section class="menu-card col-right row-3">
    <div class="menu-card__frame"></div>
    <h2 class="menu-card__title" style="top:34px">MATCHA BROWNIE</h2>
    <div class="menu-card__icon" role="img" aria-label="Brownie slice icon" style="top:92px;left:86px;width:100px;height:72px"></div>
    <div class="menu-card__price"></div>
  </section>
</body>
</html>
```